" Consultório odontológico diferenciado, sou formado há 28 anos, em fase de instalação, pequeno, mas com todos os equipamentos necessários para realizar odontologia de alto nível. "

```html
<!DOCTYPE html>
<html lang="pt-BR">
<head>
<meta charset="UTF-8">
<title>Envelope Carta — Lumen Odontologia</title>
<link rel="stylesheet" href="https://fonts.googleapis.com/css2?family=Cinzel:wght@400&family=Montserrat:wght@300;400&display=swap">
<style>
  :root {
    --stage: #e4e4e6;
    --navy: #0f1a45;
    --navy-mid: #1b2862;
    --navy-deep: #0a1235;
    --gold-light: #f3e2a6;
    --gold: #c9a55a;
    --gold-dark: #8a6a2c;
    --silver: #e8e9ef;
    --paper: #ffffff;
    --ink: #2b2f45;
    --label: #333333;
  }
  * { margin: 0; padding: 0; box-sizing: border-box; }
  html, body { width: 1200px; height: 1200px; overflow: hidden; }
  body {
    background: radial-gradient(ellipse at 50% 45%, #f4f4f5 0%, var(--stage) 75%);
    font-family: "Montserrat", sans-serif;
    position: relative;
  }
  .sheet-label {
    position: absolute; left: 29px; top: 98px;
    font-size: 17px; letter-spacing: 0.5px; color: var(--label);
  }
  .envelope {
    position: absolute; left: 269px; width: 665px;
    box-shadow: 0 6px 14px rgba(0,0,0,0.25);
    overflow: hidden;
  }
  .envelope--back {
    top: 230px; height: 377px;
    background: radial-gradient(ellipse at 50% 45%, var(--navy-mid) 0%, var(--navy) 55%, var(--navy-deep) 100%);
  }
  .gold-band {
    position: absolute; left: 0; right: 0;
    background: linear-gradient(180deg, var(--gold-dark) 0%, var(--gold-light) 35%, var(--gold) 60%, var(--gold-dark) 100%);
  }
  .envelope--back .gold-band { bottom: 0; height: 24px; }
  .brand { position: absolute; display: flex; align-items: center; }
  .brand__dot { border-radius: 50%; flex: none; }
  .brand__name { font-family: "Cinzel", serif; font-weight: 400; line-height: 1; }
  .brand__sub { font-family: "Montserrat", sans-serif; font-weight: 300; letter-spacing: 4px; }
  .envelope--back .brand { left: 150px; top: 110px; gap: 24px; }
  .envelope--back .brand__dot { width: 70px; height: 70px; background: var(--silver); }
  .envelope--back .brand__name { font-size: 62px; color: var(--silver); letter-spacing: 2px; }
  .envelope--back .brand__sub { font-size: 12px; color: var(--silver); text-align: center; margin-top: 8px; }
  .web {
    position: absolute; left: 0; right: 0; top: 306px; text-align: center;
    color: var(--silver); font-size: 17px; letter-spacing: 3.5px; font-weight: 300;
  }
  .envelope--front { top: 624px; height: 382px; background: var(--paper); }
  .flap { position: absolute; left: 0; top: 0; width: 665px; height: 84px; }
  .flap-brand {
    position: absolute; left: 0; right: 0; top: 28px;
    display: flex; justify-content: center; align-items: center; gap: 6px;
  }
  .flap-brand__dot { width: 14px; height: 14px; border-radius: 50%; background: var(--silver); }
  .flap-brand__name { font-family: "Cinzel", serif; font-size: 13px; color: var(--silver); }
  .watermark-area {
    position: absolute; left: 0; top: 84px; width: 380px; height: 260px;
    background: radial-gradient(ellipse at 30% 55%, rgba(200,205,220,0.35) 0%, rgba(255,255,255,0) 70%);
  }
  .envelope--front .brand { left: 0; right: 0; top: 244px; justify-content: center; gap: 12px; }
  .envelope--front .brand__dot { width: 30px; height: 30px; background: var(--navy); }
  .envelope--front .brand__name { font-size: 38px; color: var(--navy); }
  .contact {
    position: absolute; left: 0; right: 0; top: 300px;
    font-size: 10px; color: var(--ink); text-align: center; line-height: 1.8;
  }
  .contact .sep { color: #9aa0b8; margin: 0 10px; }
  .envelope--front .gold-band { bottom: 10px; height: 24px; }
</style>
</head>
<body>
  <p class="sheet-label">ENVELOPE CARTA</p>

  <section class="envelope envelope--back" aria-label="Verso do envelope">
    <div class="brand">
      <span class="brand__dot"></span>
      <div>
        <div class="brand__name">LUMEN</div>
        <div class="brand__sub">ODONTOLOGIA</div>
      </div>
    </div>
    <p class="web">lumenodontologia.com.br</p>
    <div class="gold-band"></div>
  </section>

  <section class="envelope envelope--front" aria-label="Frente do envelope">
    <div class="watermark-area" role="img" aria-label="Grafismo decorativo suave em tons prateados"></div>
    <svg class="flap" viewBox="0 0 665 84" aria-hidden="true">
      <defs>
        <linearGradient id="flapShade" x1="0" y1="0" x2="0" y2="1">
          <stop offset="0" stop-color="#1a2762"/>
          <stop offset="1" stop-color="#0c1540"/>
        </linearGradient>
      </defs>
      <path d="M0 0 H665 V66 L480 70 Q332 88 185 70 L0 66 Z" fill="url(#flapShade)"/>
    </svg>
    <div class="flap-brand">
      <span class="flap-brand__dot"></span>
      <span class="flap-brand__name">LUMEN</span>
    </div>
    <div class="brand">
      <span class="brand__dot"></span>
      <span class="brand__name">LUMEN</span>
    </div>
    <div class="contact">
      <p>+55 11 4000-1200<span class="sep">|</span>contato@lumenodontologia.com.br</p>
      <p>R. Aurora, 140 - Sala 12 - Jd.Sul - CEP 01000-200 / Vale Claro-SP</p>
    </div>
    <div class="gold-band"></div>
  </section>
</body>
</html>
```